Brochure Design Project for Building Designer

I need a modern and edgy brochure to introduce my new business TORV Design, Commercial and Residential Building Designers.

We specialise in Building Design, Project Management and Design Consultation.

I would like the brochure to be anywhere between 2-4 pages, depending of amount of suitable content available.
Colours to be black and white with splashes of
bright colours (mostly incorporated in photos).

Main Content of brochure to be broken up into 3 (maybe 4) sections to include:

About Us
Services
Projects

Logo Text (DESIGN etc) can be changed to white if suits better with black background.

Would be nice to include sketches to give it that architectural feel.

Samples and wording will be uploaded shortly
Updates

I HAVE PROVIDED A COMPLETE UPDATE OF PROJECT REQUIREMENTS INCLUDING ALL NEW UPLOADED FILES.

PLEASE REFER TO THE BROCHURE LAYOUT PDF UPLOADEDĀ FOR FULL INFORMATION ON PROJECT INCLUDING BROCHURE LAYOUT.

IF YOU HAVE ANY QUESTIONS OR REQUIRE ANY FURTHER INFORMATION, PLEASE LET ME KNOW

I HAVE ADDED FURTHER DEVELOPED PDF DOCUMENTS OF BROCHURE.

IF YOU HAVE TROUBLE OPENING THESE DOCS IN ADOBE ILLUSTRATOR THRU ADOBE BRIDGE PLEASE LET ME KNOW & I WILL UPLOAD AI FILES.

CAN YOU PLEASE FINE TUNE GRAPHICS AND WORK ON BACKGROUND

Target Market(s)

Builders, Property Developers, Architects, Consultants, Professionals

Industry/Entity Type

Business

Requirements
Must have
• Very Professional Look
Black and White
Simple and easy to read layout
Either A4 (if only 2 pages) or
A3 double sided with centre fold (if 4 pages)
Touch up of photos (if possible) to make them stand out of the page.
Samples of recent projects with photos
Should not have
• Any comics or similar

```html
<!DOCTYPE html>
<html lang="en">
<head>
<meta charset="utf-8">
<title>TORV Design – Brochure Cover</title>
<link rel="stylesheet" href="https://fonts.googleapis.com/css2?family=Open+Sans:wght@300;400;600&display=swap">
<style>
  :root {
    --pink: #e8408f;
    --black: #1e1c1d;
    --white: #ffffff;
    --ink: #333333;
    --plan-dark: #b9bdc0;
    --plan-mid: #dadcde;
    --plan-light: #f3f3f3;
    --render-dark: #5f5f61;
    --render-mid: #a7a7a8;
    --render-light: #e4e4e4;
  }
  * { margin: 0; padding: 0; box-sizing: border-box; }
  html, body { width: 1200px; height: 460px; overflow: hidden; background: #e6e6e6; }
  body { font-family: "Open Sans", Arial, sans-serif; }

  .brochure { display: flex; width: 1200px; height: 460px; }

  /* Back cover */
  .back-cover { position: relative; width: 600px; height: 460px; background: var(--white); overflow: hidden; }
  .back-cover__plan {
    position: absolute; left: 0; top: 0; width: 600px; height: 390px;
    background: linear-gradient(172deg, var(--plan-dark) 0%, var(--plan-mid) 40%, var(--plan-light) 75%, var(--white) 100%);
  }
  .back-cover__brand { position: absolute; left: 0; right: 0; top: 330px; text-align: center; }
  .brand-name--small { color: var(--pink); font-weight: 300; font-size: 52px; letter-spacing: 8px; line-height: 1; padding-left: 8px; }
  .brand-tagline--small { color: var(--ink); font-size: 6px; letter-spacing: 0.3px; margin-top: 4px; text-transform: uppercase; }
  .contact { position: absolute; left: 0; right: 0; top: 411px; text-align: center; color: var(--ink); font-size: 11.5px; line-height: 17px; }

  /* Front cover */
  .front-cover { position: relative; width: 600px; height: 460px; background: var(--white); overflow: hidden; }
  .front-cover__render {
    position: absolute; left: 30px; top: 104px; width: 305px; height: 276px;
    background: linear-gradient(180deg, var(--render-dark) 0%, var(--render-mid) 45%, var(--render-light) 85%, var(--white) 100%);
  }
  .front-cover__waves { position: absolute; inset: 0; }
  .sectors { position: absolute; right: 17px; top: 22px; color: var(--white); font-size: 13px; line-height: 29px; text-align: right; letter-spacing: 0.3px; }
  .front-cover__brand { position: absolute; right: 17px; top: 166px; text-align: right; }
  .brand-name--large { color: var(--pink); font-weight: 300; font-size: 120px; letter-spacing: 2px; line-height: 0.95; }
  .brand-tagline--large { color: var(--ink); font-size: 10.5px; margin-top: 8px; text-transform: uppercase; letter-spacing: 0.2px; }
  .web-address { position: absolute; right: 17px; bottom: 14px; color: var(--white); font-size: 16px; font-weight: 600; letter-spacing: 0.3px; }
</style>
</head>
<body>
<main class="brochure">
  <section class="back-cover">
    <div class="back-cover__plan" role="img" aria-label="Architectural floor plan sketch in grey lines"></div>
    <div class="back-cover__brand">
      <div class="brand-name--small">TORV</div>
      <div class="brand-tagline--small">Commercial + Residential Building Designers</div>
    </div>
    <p class="contact">
      PO Box 318, Harlow WA 6911 | Phone : 0400 123 987<br>
      Email : yourname@torvdesign.com.au | Web : www.torvdesign.com.au
    </p>
  </section>

  <section class="front-cover">
    <div class="front-cover__render" role="img" aria-label="Rendered two-storey modern building with wireframe detail"></div>
    <svg class="front-cover__waves" width="600" height="460" viewBox="0 0 600 460" aria-hidden="true">
      <path d="M0 0 H600 V86 C430 104 240 40 0 48 Z" fill="var(--black)"/>
      <path d="M0 48 C240 40 430 104 600 86 V94 C430 114 240 54 0 60 Z" fill="var(--white)"/>
      <path d="M0 60 C240 54 430 114 600 94 V102 C430 122 240 62 0 68 Z" fill="var(--pink)"/>
      <path d="M0 398 C200 410 380 386 600 396 V404 C380 394 200 420 0 406 Z" fill="var(--pink)"/>
      <path d="M0 414 C200 426 380 402 600 412 V460 H0 Z" fill="var(--black)"/>
    </svg>
    <div class="sectors">
      <div>RESIDENTIAL &nbsp;|&nbsp; MULTI-UNIT RESIDENTIAL</div>
      <div>COMMERCIAL &nbsp;|&nbsp; HEALTHCARE</div>
    </div>
    <div class="front-cover__brand">
      <div class="brand-name--large">TORV</div>
      <div class="brand-tagline--large">Commercial + Residential Building Designers</div>
    </div>
    <div class="web-address">www.torvdesign.com.au</div>
  </section>
</main>
</body>
</html>
```